Black Granite Web Design Project

We are looking for a design for a new company that will be selling Black Granite slabs and tiles. We will be selling to both end-consumers and granite installers. We have already settled on a logo and hopefully this will give an idea of what we like in our designs. We are not going to be selling online but want people to call us so the site is basically an enhanced business card. We will be focusing a lot on SEO so the design will have to keep that in mind.

We would like to keep the design in 1024x768 to make it easily view-able on all devices.

Regarding navigation there should only be a few sub-pages, like "Granite Slabs", "Granite Tiles", "Delivery", "Contact"

Aside from that we are open to designs. One idea we did have was to personalize the site and have a person there somehow to represent the company, making the user feel there are real people behind this site. This is just an idea and not a must.

The name of the company and site is "Copper Ridge Pietra"

Thanks
Updates

Hello All,

Thanks for the great designs. There are some good looking designs that show beautiful kitchens but this site is made for the granite installers and not the retail consumers. So in order not to to confuse the buyers I would like to keep this as much about the raw products as possible. The raw products being the granite slabs, thereby making it obvious we don't sell granite counter tops. 

This design will really be the identity of this company so it is important we get the right message across on this index page and that this page is as complete as possible.

Again, thanks for all the work being put into this.

Target Market(s)

The target audience is granite installers or companies that would with granite slabs.

Industry/Entity Type

Business

```html
<!DOCTYPE html>
<html lang="en">
<head>
<meta charset="utf-8">
<title>Copper Ridge Pietra</title>
<link rel="stylesheet" href="https://fonts.googleapis.com/css2?family=Open+Sans:wght@400;600;700;800&display=swap">
<style>
:root{
  --ink:#2a2d30;
  --dark:#2b2e31;
  --darker:#222427;
  --green:#2f5a3b;
  --green-dark:#244a30;
  --page:#f3f3f2;
  --white:#ffffff;
  --text:#555;
  --rule:#e4e4e4;
  --foot-text:#e8e8e8;
}
*{box-sizing:border-box;margin:0;padding:0}
html,body{width:751px;height:1200px;overflow:hidden}
body{position:relative;background:var(--page);font-family:Arial,Helvetica,sans-serif;color:var(--text)}
.abs{position:absolute}

.topbar{left:0;top:0;width:751px;height:34px;background:var(--dark)}
.topbar .social-dot{position:absolute;top:11px;width:12px;height:12px;background:#fff;border-radius:2px}

.header{left:0;top:34px;width:751px;height:42px;background:var(--white);border-bottom:1px solid #cfcfcf}
.brand{position:absolute;left:30px;top:9px;display:flex;align-items:center;gap:8px}
.brand-mark{width:24px;height:24px;background:var(--ink)}
.brand-name{font-family:'Open Sans',sans-serif;font-weight:800;font-size:15px;color:var(--ink);letter-spacing:-.3px}
.nav{position:absolute;top:17px;font-family:'Open Sans',sans-serif;font-weight:700;font-size:9.4px;color:var(--ink);white-space:nowrap}
.nav.active{color:var(--green)}

.hero{left:0;top:76px;width:751px;height:342px;
  background:
    linear-gradient(90deg,rgba(10,10,10,.85) 0 6%,transparent 8% 92%,rgba(20,20,20,.9) 95%),
    linear-gradient(180deg,#d6d6d6 0%,#cfcfcf 4%,#1c1c1e 4.5% 22%,#a9a9a9 26%,#9c9c9c 44%,#b9b9b9 47%,#151517 50%,#0c0c0d 80%,#8c8c8c 84%,#b3b3b3 100%)}
.dots{left:340px;top:374px;display:flex;gap:6px}
.dots span{width:9px;height:9px;border:1px solid #3a3a3a;border-radius:50%;background:transparent}
.dots span.on{background:var(--green);border-color:var(--green)}

.card{left:30px;top:386px;width:692px;height:586px;background:var(--white)}

.intro-icon{width:22px;height:21px;background:var(--green)}
.intro-title{font-family:'Open Sans',sans-serif;font-size:16px;color:#222;white-space:nowrap}
.intro-body{font-size:10.3px;line-height:13.6px;color:#555;white-space:nowrap}
.vdivider{left:375px;top:408px;width:1px;height:72px;background:var(--rule)}

.section-tab{height:22px;background:var(--green);font-family:'Open Sans',sans-serif;font-weight:700;font-size:12px;color:#fff;padding:2px 0 0 8px;white-space:nowrap}
.section-tab::after{content:"";position:absolute;right:2px;top:6px;width:10px;height:9px;
  background:repeating-linear-gradient(180deg,#8fb09a 0 1px,transparent 1px 3px)}
.section-rule{height:4px;border-top:1px solid #ececec;border-bottom:1px solid #ececec}

.thumb{width:153px;height:152px;background:#fff;border:1px solid #dcdcdc;padding:5px;box-shadow:0 1px 2px rgba(0,0,0,.06)}
.thumb .photo{width:100%;height:100%}

.green-line{left:0;top:949px;width:751px;height:5px;background:var(--green-dark)}
.footer{left:0;top:954px;width:751px;height:222px;background:var(--dark)}
.footer-bottom{left:0;top:1176px;width:751px;height:24px;background:var(--darker)}

.foot-head{font-family:'Open Sans',sans-serif;font-weight:700;font-size:9.6px;color:#fff;white-space:nowrap}
.foot-nav{left:30px;top:1029px;width:93px}
.foot-nav a{display:block;height:26.5px;padding-top:2px;font-family:'Open Sans',sans-serif;font-weight:700;font-size:9.4px;color:var(--foot-text);text-decoration:none;border-bottom:1px solid #44474a}

.field{background:#fff;border-radius:3px;font-family:'Open Sans',sans-serif;font-weight:700;font-size:8.6px;color:#a9a9a9;padding:4px 6px}
.send{left:162px;top:1133px;width:59px;height:20px;background:#111;border:1px solid #555;border-radius:3px;font-family:'Open Sans',sans-serif;font-weight:700;font-size:9px;color:#fff;text-align:center;line-height:18px}

.contact-lines{left:407px;top:1031px;font-family:'Open Sans',sans-serif;font-weight:700;font-size:9.2px;line-height:12.6px;color:var(--foot-text);white-space:nowrap}
.soc{top:1032px;width:21px;height:21px;border-radius:3px}
.chat{left:608px;top:1069px;width:114px;height:17px;background:#161719;font-family:'Open Sans',sans-serif;font-weight:700;font-size:9.4px;color:#fff}
.foot-brand{left:608px;top:1108px;width:114px;text-align:center;font-family:'Open Sans',sans-serif;font-weight:800;font-size:12.5px;line-height:15px;color:#fff}
.copyright{left:30px;top:1183px;font-size:8.2px;color:#cfcfcf}
</style>
</head>
<body>

<div class="abs topbar">
  <span class="social-dot" style="left:684px"></span>
  <span class="social-dot" style="left:704px"></span>
</div>

<header class="abs header">
  <div class="brand"><span class="brand-mark"></span><span class="brand-name">Copper Ridge Pietra</span></div>
  <span class="nav active" style="left:420px">HOME</span>
  <span class="nav" style="left:458px">GRANITE SLABS</span>
  <span class="nav" style="left:541px">GRANITE TILES</span>
  <span class="nav" style="left:619px">DELIVERY</span>
  <span class="nav" style="left:679px">CONTACT</span>
</header>

<div class="abs hero" role="img" aria-label="Kitchen with grey speckled granite backsplash, glossy black granite cabinets and a grey stone floor"></div>

<div class="abs card"></div>
<div class="abs dots"><span></span><span></span><span class="on"></span><span></span><span></span></div>

<svg class="abs intro-icon" style="left:50px;top:402px" viewBox="0 0 22 21"><rect width="22" height="21" fill="#2f5a3b"/><circle cx="11" cy="8" r="3.2" fill="#fff"/><path d="M5 17c0-3.5 2.7-5 6-5s6 1.5 6 5z" fill="#fff"/></svg>
<div class="abs intro-title" style="left:84px;top:404px">Copper Ridge Pietra</div>
<p class="abs intro-body" style="left:50px;top:434px">We will be selling Black Granite slabs and tiles. We will be selling<br>to both end-consumers and granite installers. We have already<br>settled on a logo and hopefully this will give an idea of what we like<br>in our designs.-This for Example</p>

<div class="abs vdivider"></div>

<svg class="abs intro-icon" style="left:406px;top:402px" viewBox="0 0 22 21"><rect width="22" height="21" fill="#2f5a3b"/><circle cx="11" cy="10.5" r="4.6" fill="none" stroke="#fff" stroke-width="2.4" stroke-dasharray="2 1.6"/><circle cx="11" cy="10.5" r="1.6" fill="#fff"/></svg>
<div class="abs intro-title" style="left:441px;top:404px">Our Granite</div>
<p class="abs intro-body" style="left:406px;top:434px">We are not going to be selling online but want people to call us so<br>the site is basically an enhanced business card. We will be<br>focusing a lot on SEO so the design will have to keep that in<br>mind.-This For Example</p>

<div class="abs section-tab" style="left:46px;top:524px;width:115px">Granite Slabs</div>
<div class="abs section-rule" style="left:161px;top:532px;width:541px"></div>

<div class="abs thumb" style="left:46px;top:562px"><div class="photo" role="img" aria-label="Raw black granite slab with swirling white and gold veins" style="background:radial-gradient(ellipse at 65% 40%,#8a8378 0%,#4a4641 30%,transparent 60%),linear-gradient(135deg,#1b1b1b,#3e3b37 45%,#6e6658 70%,#161616)"></div></div>
<div class="abs thumb" style="left:214px;top:562px"><div class="photo" role="img" aria-label="Black granite slab with fine silvery white streaks" style="background:linear-gradient(165deg,#6c6a66 0 3%,#1c1d21 5%,#2b2d33 40%,#3b3e46 55%,#1a1b1e 80%,#121214)"></div></div>
<div class="abs thumb" style="left:382px;top:562px"><div class="photo" role="img" aria-label="Polished absolute black granite slab standing in a stone yard" style="background:linear-gradient(180deg,#5a4c3e 0,#3a3630 10%,#101011 14%,#0d0d0e 70%,#1b1b1c 100%)"></div></div>
<div class="abs thumb" style="left:549px;top:562px"><div class="photo" role="img" aria-label="Glossy black granite slab reflecting warehouse lights" style="background:linear-gradient(180deg,#7c8186 0,#4b4f53 8%,#1d1f21 14%,#15171a 60%,#0f1011 100%)"></div></div>

<div class="abs section-tab" style="left:46px;top:751px;width:99px">Granite Tiles</div>
<div class="abs section-rule" style="left:145px;top:759px;width:557px"></div>

<div class="abs thumb" style="left:46px;top:789px"><div class="photo" role="img" aria-label="Bathroom finished in dark grey granite wall and floor tiles" style="background:linear-gradient(180deg,#4a5058 0,#3a4048 55%,#2f343a 75%,#5a6068 100%)"></div></div>
<div class="abs thumb" style="left:214px;top:789px"><div class="photo" role="img" aria-label="Shower room with polished black granite floor tiles" style="background:linear-gradient(180deg,#c9cdd0 0,#9ea3a7 35%,#3a3d40 55%,#121315 70%,#1f2022 100%)"></div></div>
<div class="abs thumb" style="left:382px;top:789px"><div class="photo" role="img" aria-label="Kitchen with white cabinets and dark granite floor tiles" style="background:linear-gradient(180deg,#5a5e60 0,#d6dadc 25%,#e6e9ea 55%,#9da2a5 78%,#5e6467 100%)"></div></div>
<div class="abs thumb" style="left:549px;top:789px"><div class="photo" role="img" aria-label="Lounge with polished black granite floor under warm lights" style="background:linear-gradient(180deg,#8b6a3d 0,#3a3f55 25%,#1f3550 45%,#0e1628 70%,#070a12 100%)"></div></div>

<div class="abs green-line"></div>
<div class="abs footer"></div>
<div class="abs card" style="top:949px;height:23px"></div>

<div class="abs foot-head" style="left:30px;top:1004px">NAVIGATION</div>
<nav class="abs foot-nav">
  <a href="#">Home</a><a href="#">Granite Slabs</a><a href="#">Granite Tiles</a><a href="#">Delivery</a><a href="#">Contact</a>
</nav>

<div class="abs foot-head" style="left:162px;top:1004px">QUICK INQUIRY</div>
<div class="abs field" style="left:162px;top:1033px;width:200px;height:21px">Name:</div>
<div class="abs field" style="left:162px;top:1063px;width:200px;height:22px">Email:</div>
<div class="abs field" style="left:162px;top:1092px;width:200px;height:34px">Message:</div>
<div class="abs send">Send It</div>

<div class="abs foot-head" style="left:407px;top:1004px">CONTACT DETAILS</div>
<div class="abs contact-lines">
  Lorem Ipsum Dolor,<br>Lorem Ipsum Dolo, Lorem Ipsum<br>Dolo- XXXXX<br>YYYYYYYY<br><br>
  Ph.: +11 123456789<br>Email: sales@copperridgepietra.com<br>Fax: +11-111-1111111<br>Ph.: +11-111-1111111
</div>

<div class="abs foot-head" style="left:607px;top:1004px">CONTACT US VIA SOCIAL</div>
<span class="abs soc" style="left:607px;background:#3b5b9a"></span>
<span class="abs soc" style="left:639px;background:#3fa7dc"></span>
<svg class="abs soc" style="left:670px" viewBox="0 0 21 21"><rect width="21" height="21" rx="3" fill="#d8d8d8"/><rect x="2" y="5" width="17" height="11" fill="#f4f4f4" stroke="#9a9a9a"/><path d="M2 5l8.5 6 8.5-6" fill="none" stroke="#9a9a9a"/></svg>
<span class="abs soc" style="left:700px;background:#cb2027"></span>

<div class="abs chat">
  <svg class="abs" style="left:5px;top:3px" width="10" height="11" viewBox="0 0 10 11"><circle cx="5" cy="3" r="2.5" fill="#fff"/><path d="M0 11c0-3 2.2-4.5 5-4.5S10 8 10 11z" fill="#fff"/></svg>
  <span class="abs" style="left:21px;top:2px">Live chat</span>
  <span class="abs" style="left:92px;top:0;width:1px;height:17px;background:#444"></span>
  <svg class="abs" style="left:99px;top:3px" width="10" height="10" viewBox="0 0 10 10"><path d="M5 0v10M0 5h10" stroke="#fff" stroke-width="2"/></svg>
</div>
<div class="abs foot-brand">Copper Ridge<br>Pietra</div>

<div class="abs footer-bottom"></div>
<div class="abs copyright">Copyright © 2013 Copper Ridge Pietra</div>

</body>
</html>
```